Need a Zine cover designed

I’m looking for someone who can design an eye catching and original zine cover. Incorporating the logo I included below. I’m not 100% sure which logo I want to use on the cover, if it’s possible to see how you incorporate the logos on a sample will make it easier for me to decide. Thank you for your time.
For the second logo I’m unsure how to remove the grey background, but I do not want it included in the zine cover
The title of the zine is:
Amber Crossroads
perspectives of culture, life, & love

```html
<!DOCTYPE html>
<html lang="en">
<head>
<meta charset="utf-8">
<title>Amber Crossroads — Zine Cover</title>
<link href="https://fonts.googleapis.com/css2?family=Jost:wght@300;500;600&display=swap" rel="stylesheet">
<style>
  :root {
    --paper: #ffffff;
    --title-grey: #58595b;
    --warm-red: #d9432b;
    --amber: #e8952f;
    --leaf: #9cc95a;
    --sky: #3aaed8;
    --club-blue: #3a9fc7;
  }
  html, body {
    margin: 0;
    padding: 0;
    overflow: hidden;
    background: var(--paper);
  }
  .cover {
    position: relative;
    width: 873px;
    height: 1200px;
    background: var(--paper);
    overflow: hidden;
    font-family: "Jost", "Futura", sans-serif;
  }
  .wave-field {
    position: absolute;
    inset: 0;
    width: 873px;
    height: 1200px;
  }
  .title {
    position: absolute;
    left: 150px;
    top: 128px;
    margin: 0;
    font-weight: 300;
    font-size: 100px;
    line-height: 1.12;
    letter-spacing: 1px;
    color: var(--title-grey);
    text-transform: uppercase;
  }
  .title span { display: block; }
  .tagline {
    position: absolute;
    left: 151px;
    top: 398px;
    margin: 0;
    padding: 4px 12px 3px;
    background: linear-gradient(90deg, var(--warm-red), var(--amber) 35%, var(--leaf) 65%, var(--sky));
    color: var(--paper);
    font-weight: 500;
    font-size: 24px;
    letter-spacing: 0.5px;
    text-transform: uppercase;
    white-space: nowrap;
  }
  .club-name {
    position: absolute;
    left: 250px;
    top: 890px;
    width: 370px;
    margin: 0;
    text-align: center;
    font-weight: 600;
    font-size: 50px;
    line-height: 1.05;
    color: var(--club-blue);
  }
</style>
</head>
<body>
  <main class="cover">
    <svg class="wave-field" viewBox="0 0 873 1200" xmlns="http://www.w3.org/2000/svg">
      <defs>
        <linearGradient id="corner-tone" x1="0" y1="0" x2="1" y2="1">
          <stop offset="0" stop-color="#cfe3a8" stop-opacity="0.35"/>
          <stop offset="1" stop-color="#9fd6e8" stop-opacity="0.35"/>
        </linearGradient>
        <linearGradient id="flow-tone" x1="1" y1="0" x2="0" y2="1">
          <stop offset="0" stop-color="#8fd0ea" stop-opacity="0.35"/>
          <stop offset="0.6" stop-color="#bfe2ee" stop-opacity="0.3"/>
          <stop offset="1" stop-color="#e9d9b0" stop-opacity="0.35"/>
        </linearGradient>
      </defs>
      <path role="img" aria-label="Flowing contour-line pattern in green and blue, top left corner"
            fill="url(#corner-tone)"
            d="M0 0 H285 C300 60 230 90 215 150 C200 220 240 280 170 330 C120 365 60 370 0 395 Z"/>
      <path role="img" aria-label="Flowing contour-line pattern in blue fading to sand, right side and bottom"
            fill="url(#flow-tone)"
            d="M873 222 C760 230 680 320 640 440 C610 540 650 620 560 700 C470 780 430 850 470 960 C500 1040 430 1120 400 1200 H873 Z"/>
    </svg>

    <h1 class="title"><span>Amber</span><span>Crossroads</span></h1>
    <p class="tagline">Perspectives of culture, life, &amp; love</p>

    <p class="club-name">Mellow Fellows<br>Club</p>
  </main>
</body>
</html>
```